Presence Leadership Model

I am looking for a graphic design of the attached leadership model. The colors and design can be altered in any manner that brings the model alive version of the house model.

```html
<!DOCTYPE html>
<html lang="en">
<head>
<meta charset="UTF-8">
<title>Presence Leadership Model</title>
<link href="https://fonts.googleapis.com/css2?family=Open+Sans:wght@400;500;600;700&display=swap" rel="stylesheet">
<style>
  :root {
    --roof: #64b0b6;
    --band: #43a0a8;
    --org-head: #c81f30;
    --org-body: #e3485a;
    --int-head: #f47a08;
    --int-body: #fb8c26;
    --per-head: #0e4468;
    --per-body: #0a5685;
    --per-base: #0d4266;
    --inner-band: #222222;
    --inner-cell: #3a3a3a;
    --accent: #f6c51b;
    --white: #ffffff;
  }
  * { margin: 0; padding: 0; box-sizing: border-box; }
  html, body { width: 1200px; height: 675px; overflow: hidden; background: var(--white); }
  body { font-family: "Open Sans", Arial, sans-serif; color: var(--white); }
  .model { position: relative; width: 1200px; height: 675px; }
  .model-shapes { position: absolute; inset: 0; }

  .roof-text { position: absolute; left: 174px; width: 852px; top: 56px; text-align: center; }
  .roof-title { font-size: 28px; font-weight: 700; line-height: 36px; }
  .roof-sub { font-size: 21px; line-height: 28px; font-weight: 400; }

  .band-label { position: absolute; left: 225px; width: 750px; text-align: center; font-size: 19px; font-weight: 700; }
  .band-outer { top: 168px; line-height: 30px; }
  .band-inner { top: 565px; line-height: 32px; }

  .pillar-head { position: absolute; top: 214px; width: 200px; text-align: center; }
  .pillar-title { font-size: 20px; font-weight: 700; line-height: 26px; white-space: nowrap; }
  .pillar-method { font-size: 20px; line-height: 25px; text-decoration: underline; text-underline-offset: 3px; text-decoration-thickness: 1px; }

  .pillar-list { position: absolute; list-style: none; font-size: 15.5px; line-height: 18.75px; font-weight: 600; letter-spacing: -0.2px; }
  .pillar-list li { position: relative; padding-left: 11px; white-space: nowrap; }
  .pillar-list li::before { content: "•"; position: absolute; left: 0; top: 0; font-size: 15px; }
  .list-org { left: 273px; top: 285px; }
  .list-int { left: 529px; top: 285px; }
  .list-per { left: 782px; top: 284px; line-height: 20px; }
  .list-per li { margin-bottom: 10px; }

  .wellbeing { position: absolute; top: 598px; list-style: none; font-size: 15.5px; line-height: 19px; font-weight: 600; color: var(--accent); }
  .wellbeing li { position: relative; padding-left: 12px; white-space: nowrap; }
  .wellbeing li::before { content: "•"; position: absolute; left: 0; font-size: 15px; }
</style>
</head>
<body>
<main class="model">
  <svg class="model-shapes" width="1200" height="675" viewBox="0 0 1200 675" aria-hidden="true">
    <defs>
      <pattern id="dot-grid" width="4" height="4" patternUnits="userSpaceOnUse">
        <circle cx="2" cy="2" r="1.1" fill="#111"/>
      </pattern>
    </defs>
    <polygon points="600,16 1026,136 1026,157 174,157 174,136" fill="var(--roof)"/>
    <rect x="225" y="166" width="750" height="33" fill="var(--band)"/>

    <polygon points="239,208 447,208 437,275 249,275" fill="var(--org-head)"/>
    <polygon points="266,275 429,275 442,536 252,536" fill="var(--org-body)"/>
    <rect x="251" y="536" width="191" height="25" fill="var(--org-head)"/>

    <polygon points="496,208 703,208 694,275 505,275" fill="var(--int-head)"/>
    <polygon points="521,275 684,275 697,536 507,536" fill="var(--int-body)"/>
    <rect x="507" y="536" width="190" height="25" fill="var(--int-head)"/>

    <polygon points="746,208 953,208 944,275 755,275" fill="var(--per-head)"/>
    <polygon points="770,275 933,275 947,536 756,536" fill="var(--per-body)"/>
    <rect x="756" y="536" width="191" height="25" fill="var(--per-base)"/>

    <polygon points="443,381 463,362 463,373 506,373 506,389 463,389 463,400" fill="url(#dot-grid)"/>
    <polygon points="694,381 714,362 714,373 757,373 757,389 714,389 714,400" fill="url(#dot-grid)"/>

    <rect x="225" y="564" width="750" height="34" fill="var(--inner-band)"/>
    <rect x="225" y="598" width="248" height="47" fill="var(--inner-cell)"/>
    <rect x="476" y="598" width="246" height="47" fill="var(--inner-cell)"/>
    <rect x="725" y="598" width="250" height="47" fill="var(--inner-cell)"/>
  </svg>

  <header class="roof-text">
    <h1 class="roof-title">Presence</h1>
    <p class="roof-sub">Foster contagious success through people,<br>relationships and a shared vision</p>
  </header>

  <h2 class="band-label band-outer">Outer (Impact) Strategies</h2>

  <div class="pillar-head" style="left:243px;">
    <div class="pillar-title">Organization Level</div>
    <div class="pillar-method">Wins Theory</div>
  </div>
  <div class="pillar-head" style="left:500px;">
    <div class="pillar-title">Interpersonal Level</div>
    <div class="pillar-method">Heart Listening</div>
  </div>
  <div class="pillar-head" style="left:750px;">
    <div class="pillar-title">Personal Level</div>
    <div class="pillar-method">Mindful Exchange</div>
  </div>

  <ul class="pillar-list list-org">
    <li>Develop concrete<br>outcomes, and<br>visible results</li>
    <li>Foster in-depth<br>changes, and new<br>practices</li>
    <li>Have a micro,<br>interpersonal or<br>local impact</li>
    <li>Cultivate positive<br>judgement, and<br>shared ambition</li>
  </ul>

  <ul class="pillar-list list-int">
    <li>Ask open-ended<br>questions</li>
    <li>Affirm someone’s<br>strengths, efforts<br>and past success</li>
    <li>Reflect back what<br>is shared for<br>confirmation</li>
    <li>Summarize key<br>points to gain<br>insights</li>
    <li>Share and develop<br>mutual expertise</li>
  </ul>

  <ul class="pillar-list list-per">
    <li>Breathe</li>
    <li>Settle</li>
    <li>Notice</li>
    <li>Stay with<br>What Arises</li>
    <li>Hear Fully</li>
    <li>Speak Honestly</li>
  </ul>

  <h2 class="band-label band-inner">Inner (Wellbeing) Strategies</h2>

  <ul class="wellbeing" style="left:279px;">
    <li>Physical Fitness</li>
    <li>Nutrition</li>
  </ul>
  <ul class="wellbeing" style="left:521px;">
    <li>Heart Rate Variability</li>
    <li>Neurofeedback</li>
  </ul>
  <ul class="wellbeing" style="left:774px;">
    <li>Coastal Hiking Club</li>
    <li>Video Gaming Club</li>
  </ul>
</main>
</body>
</html>
```